Bref créative
Business cards and stationary Hospitality group company in Mexico
subtitle is optional "Hospitalidad Hecho en Mexico"
I need double sided standard sized Business Card [3.5" x 2"]
I like the fonts used in my logo but we are open to new fonts or more than one if necessary
Modern
Gerardo Villena
4871 Almendros
Col. Santa Brígida
Monterrey, NL México
CP 67215
beto@qvral.mx
www.qvral.mx
I am looking for a modern design, I like those colors but feel free to play with the colors if you have an idea..
QV ALBERGANTE

```html
<!DOCTYPE html>
<html lang="es">
<head>
<meta charset="utf-8">
<title>QV Albergante – Papelería</title>
<link href="https://fonts.googleapis.com/css2?family=Montserrat:wght@400;600;700&display=swap" rel="stylesheet">
<style>
  :root{
    --orange:#f04a23;
    --orange-light:#f6703f;
    --charcoal:#2a2a2a;
    --paper:#ffffff;
    --ground:#f4f4f4;
    --faint:#ececec;
    --muted:#6f6f6f;
  }
  *{margin:0;padding:0;box-sizing:border-box}
  html,body{width:1200px;height:936px;overflow:hidden;background:var(--ground);font-family:'Montserrat',sans-serif}
  .canvas{position:relative;width:1200px;height:936px}
  .sheet{position:absolute;background:var(--paper);overflow:hidden;box-shadow:0 2px 6px rgba(0,0,0,.12)}

  .brand{display:flex;align-items:center;gap:6px;color:var(--paper);font-weight:700;letter-spacing:.08em;white-space:nowrap}
  .brand__mark{background:var(--orange);flex:none}

  /* letterhead */
  .letterhead{left:185px;top:61px;width:355px;height:556px}
  .letterhead__band{position:absolute;left:0;top:40px;width:100%;height:52px;background:var(--charcoal)}
  .letterhead__rule{position:absolute;left:0;top:96px;width:100%;height:3px;background:var(--orange)}
  .letterhead .brand{position:absolute;left:18px;top:58px;font-size:11px}
  .letterhead .brand__mark{width:9px;height:9px}
  .letterhead__watermark{position:absolute;left:0;top:210px;width:100%;text-align:center;color:var(--faint);font-weight:700;font-size:26px;letter-spacing:.08em}
  .letterhead__footer{position:absolute;left:0;bottom:22px;width:100%;text-align:center;font-size:6.5px;line-height:1.6;color:var(--muted)}

  /* letterhead reverse */
  .reverse{left:632px;top:38px;width:462px;height:581px;background:radial-gradient(ellipse at 50% 45%,var(--orange-light),var(--orange) 75%)}
  .reverse__band{position:absolute;left:0;top:206px;width:100%;height:162px;background:var(--charcoal);border-top:2px solid rgba(255,255,255,.5);border-bottom:2px solid rgba(255,255,255,.5);display:flex;align-items:center;justify-content:center}
  .reverse .brand{font-size:22px}
  .reverse .brand__mark{width:16px;height:16px}

  /* business cards */
  .card{left:43px;width:175px;height:93px;background:var(--charcoal)}
  .card--front{top:667px}
  .card--back{top:784px}
  .card .brand{position:absolute;left:9px;top:12px;font-size:7.5px}
  .card .brand__mark{width:6px;height:6px}
  .card__strip{position:absolute;left:0;top:44px;width:100%;height:22px;background:var(--orange);color:var(--paper);padding:3px 9px}
  .card__name{font-size:7px;font-weight:700;letter-spacing:.04em}
  .card__role{font-size:5px}
  .card__contact{position:absolute;left:9px;top:71px;font-size:4.6px;line-height:1.5;color:#cfcfcf}
  .card--back .brand{top:54px;font-size:8px}
  .card__line{position:absolute;left:0;top:48px;width:100%;height:2px;background:var(--orange)}

  /* envelope front */
  .envelope{left:264px;top:667px;width:429px;height:218px}
  .envelope__band{position:absolute;left:0;top:18px;width:100%;height:48px;background:var(--charcoal)}
  .envelope__rule{position:absolute;left:0;top:69px;width:100%;height:2px;background:var(--orange)}
  .envelope .brand{position:absolute;left:14px;top:35px;font-size:9px}
  .envelope .brand__mark{width:8px;height:8px}

  /* envelope back */
  .envelope-back{left:738px;top:667px;width:432px;height:218px}
  .envelope-back svg{position:absolute;left:0;top:0}
  .envelope-back__url{position:absolute;left:0;top:30px;width:100%;text-align:center;color:var(--paper);font-size:13px;letter-spacing:.16em}
  .envelope-back__url b{font-weight:700}
</style>
</head>
<body>
<main class="canvas">

  <section class="sheet letterhead">
    <div class="letterhead__band"></div>
    <div class="letterhead__rule"></div>
    <div class="brand"><span class="brand__mark"></span>QV ALBERGANTE</div>
    <div class="letterhead__watermark">QV ALBERGANTE</div>
    <p class="letterhead__footer">4871 Almendros Col. Santa Brígida Monterrey, NL México CP 67215<br>(81) 5550 1234 · (81) 5550 5678 · beto@qvral.mx · www.qvral.mx</p>
  </section>

  <section class="sheet reverse">
    <div class="reverse__band">
      <div class="brand"><span class="brand__mark"></span>QV ALBERGANTE</div>
    </div>
  </section>

  <section class="sheet card card--front">
    <div class="brand"><span class="brand__mark"></span>QV ALBERGANTE</div>
    <div class="card__strip">
      <p class="card__name">Gerardo Villena</p>
      <p class="card__role">Director General</p>
    </div>
    <p class="card__contact">4871 Almendros, Col. Santa Brígida, CP 67215<br>beto@qvral.mx · www.qvral.mx</p>
  </section>

  <section class="sheet card card--back">
    <div class="card__line"></div>
    <div class="brand"><span class="brand__mark"></span>QV ALBERGANTE</div>
  </section>

  <section class="sheet envelope">
    <div class="envelope__band"></div>
    <div class="envelope__rule"></div>
    <div class="brand"><span class="brand__mark"></span>QV ALBERGANTE</div>
  </section>

  <section class="sheet envelope-back">
    <svg width="432" height="218" viewBox="0 0 432 218" aria-hidden="true">
      <path d="M0 0H432V70Q216 112 0 70Z" fill="var(--orange)"/>
    </svg>
    <p class="envelope-back__url">www.<b>qvral</b>.mx</p>
  </section>

</main>
</body>
</html>
```